Business Performance Improvement Book Cover Design Project

We need a book cover design for a new company, based in Eastern Australia, called Varrow Global. We advise clients on process improvement, continuous improvement and business performance improvement, especially in the manufacturing areas and Fast Moving Consumer Goods industries.
We have a written a book designed to demonstrate our very high calibre of knowledge and to use as a marketing tool for prospective clients. We hope to give it out at training seminars and as a comprehensive business card.

Title of the book is: An integrated path to Operational Results Growth.
Subtitle: Shape a Steady Progress method to match your workplace values.
Author: by Martin Varrow
Back Cover: No need for a bar code in this edition. An important aspect is that we will distribute by hand. Text below for back page.

'For the experienced Business Performers, this book is designed to offer an insight into the advantages and an example of an approach to Business Improvement. It is not the only way but it is tried and tested in world class companies and it works. For those new to Continuous Improvement, it offers a helpful introduction to a holistic business improvement system, an overview of important success factors and pitfalls, recommendations on how to implement tools and methods and a quick guide to see when to use which tools. '

'Consultancies are one of many tools management teams can engage and management must make sure the consultants tailor their approach to suit its business needs and culture and not vice versa.'

End of text for back cover.

Business Performance Improvement is also known as or can include:
Continuous Improvement
Process Improvement
Lean Six Sigma
Operational Excellence
Total Productive Maintenance
Harlow Assembly Method
Total Quality Management
Business Process Re engineering
Output Levers
=
Varrow Global

The book size is 175 x 240 mm and will need a 10-15mm bleed. The spine is not known at this stage exactly and will need to be updated once the printing is finished but I suggest a 10mm until I have the exact size.

Our company colours are Pantone 288, R0,G75,B141, C100,M79,Y17,K3. Attached are some other publications that give a sense of what we like to portray, Some words which might add to this are: professional, elegance, quality, sleek.

Reason: After receiving the designs, I realised that I needed to update the brief with more and better quality information for designers to work with.

Target Market(s)

people in the accounting and insolvency industries, production managers and CEOs, Chief Operating Officers, members of the executive team of large companies and GMs of small companies.

Industry/Entity Type

Marketing

Requirements
Must have
• Communicate an image that shows an improvement or increase of something.
Very professional and elegant
Emphasis on the words 'Business Performance Improvement' in the title, subtitle also important
Must appeal to a high-end of the market audience
Nice to have
• Recommendation for your cover to be gloss or matt in print
Image can be indirectly related to money but not specifically
Somehow that it matches or is not so different to the attached brochure
Should not have
• Not be too loud or commercial
Book jacket. WIll be printed as soft cover first run and hard cover 2nd run

```html
<!DOCTYPE html>
<html lang="en">
<head>
<meta charset="utf-8">
<title>An Integrated Path to Operational Results Growth – Cover Spread</title>
<link href="https://fonts.googleapis.com/css2?family=Roboto+Condensed:wght@700;800;900&family=Open+Sans:wght@400;600&display=swap" rel="stylesheet">
<style>
  :root {
    --brand-blue: #004b8d;
    --title-blue: #0d3f8f;
    --band-blue: #123f8c;
    --panel-blue: rgba(20, 58, 138, 0.9);
    --sky-top: #5f93c9;
    --sky-mid: #9fc1e3;
    --cloud: #e6edf3;
    --horizon: #dfe6dc;
    --money-light: #d3dccb;
    --money-mid: #a3b59a;
    --money-dark: #6a7d63;
    --boat-cream: #eef0e2;
    --boat-green: #bfcbb0;
    --page-bg: #eceef0;
    --text-dark: #1d232a;
    --white: #ffffff;
  }
  * { box-sizing: border-box; margin: 0; padding: 0; }
  html, body { width: 1200px; height: 800px; overflow: hidden; }
  body { background: var(--page-bg); font-family: "Open Sans", Arial, sans-serif; }

  .cover-spread {
    position: absolute; left: 120px; top: 80px;
    width: 961px; height: 640px; display: flex;
    box-shadow: 0 6px 24px rgba(0,0,0,0.18);
  }
  .back-cover, .front-cover { position: relative; width: 467px; height: 640px; overflow: hidden; }
  .spine { position: relative; width: 27px; height: 640px; overflow: hidden; }

  .sky-photo {
    position: absolute; left: 0; right: 0; top: 0; height: 380px;
    background:
      radial-gradient(ellipse 60% 18% at 30% 62%, rgba(255,255,255,0.85), rgba(255,255,255,0) 70%),
      radial-gradient(ellipse 55% 14% at 80% 45%, rgba(255,255,255,0.7), rgba(255,255,255,0) 70%),
      linear-gradient(180deg, var(--sky-top) 0%, var(--sky-mid) 40%, var(--cloud) 75%, var(--horizon) 100%);
  }
  .money-photo {
    position: absolute; left: 0; right: 0; top: 380px; bottom: 0;
    background:
      radial-gradient(ellipse 40% 20% at 25% 30%, rgba(230,236,222,0.8), rgba(230,236,222,0) 70%),
      radial-gradient(ellipse 45% 22% at 75% 60%, rgba(220,228,210,0.7), rgba(220,228,210,0) 70%),
      linear-gradient(180deg, var(--money-light) 0%, var(--money-mid) 45%, var(--money-dark) 100%);
  }
  .boat-photo {
    position: absolute; left: 78px; top: 250px; width: 330px; height: 120px;
    background: radial-gradient(ellipse 50% 50% at 50% 55%, var(--boat-cream) 0%, var(--boat-green) 55%, rgba(191,203,176,0) 100%);
  }

  .title-block { position: absolute; left: 0; right: 0; text-align: center; font-family: "Roboto Condensed", "Arial Narrow", sans-serif; color: var(--title-blue); text-transform: uppercase; }
  .title-outline { text-shadow: -2px -2px 0 var(--white), 2px -2px 0 var(--white), -2px 2px 0 var(--white), 2px 2px 0 var(--white), 0 2px 0 var(--white), 0 -2px 0 var(--white), 2px 0 0 var(--white), -2px 0 0 var(--white); }
  .title-line { display: block; font-weight: 900; line-height: 1; }
  .subtitle { margin: 7px auto 0; font-weight: 700; color: var(--text-dark); letter-spacing: 2px; line-height: 1.3; border-top: 1px dashed #44505c; padding-top: 6px; }

  .front-cover .title-block { top: 26px; }
  .front-cover .title-line.small { font-size: 38px; }
  .front-cover .title-line.large { font-size: 58px; }
  .front-cover .subtitle { width: 400px; font-size: 12.5px; }

  .author-band {
    position: absolute; left: 0; right: 0; bottom: 0; height: 26px;
    background: var(--band-blue); color: var(--white);
    font-family: "Roboto Condensed", "Arial Narrow", sans-serif; font-weight: 700;
    font-size: 13px; letter-spacing: 1px; text-align: center; line-height: 26px;
  }

  .back-cover .title-block { top: 14px; }
  .back-cover .author-possessive {
    display: block; text-align: right; padding-right: 34px; margin-bottom: 4px;
    font-size: 10px; font-weight: 800; color: var(--text-dark); letter-spacing: 0.5px;
    text-shadow: -1px 0 0 var(--white), 1px 0 0 var(--white), 0 1px 0 var(--white), 0 -1px 0 var(--white);
  }
  .back-cover .title-line.small { font-size: 33px; }
  .back-cover .title-line.large { font-size: 50px; }
  .back-cover .subtitle { width: 350px; font-size: 10.5px; }

  .also-known-panel {
    position: absolute; left: 40px; top: 222px; width: 387px; height: 290px;
    background: var(--panel-blue); color: var(--white);
    text-align: center; padding-top: 16px; font-size: 14px; line-height: 1.36;
  }
  .also-known-panel .intro { margin: 0 24px 10px; }
  .also-known-panel ul { list-style: none; }
  .also-known-panel .company-result { font-size: 16px; margin-top: 2px; }

  .publisher-mark { position: absolute; left: 30px; top: 542px; display: flex; align-items: center; gap: 8px; }
  .publisher-mark .mark-dot { width: 18px; height: 18px; border-radius: 50%; background: var(--brand-blue); }
  .publisher-mark .mark-name { font-family: "Open Sans", Arial, sans-serif; font-weight: 600; font-size: 22px; color: var(--brand-blue); }

  .isbn-box {
    position: absolute; right: 34px; top: 530px; width: 134px; height: 64px;
    background: var(--band-blue); color: var(--white);
    font-size: 17px; font-weight: 600; display: flex; align-items: center; justify-content: center;
  }
  .back-band { position: absolute; left: 0; right: 0; bottom: 0; height: 26px; background: var(--band-blue); }

  .spine-text {
    position: absolute; left: 50%; top: 50%;
    transform: translate(-50%, -50%) rotate(90deg);
    white-space: nowrap; font-family: "Roboto Condensed", "Arial Narrow", sans-serif;
    font-weight: 900; font-size: 12.5px; color: var(--title-blue); text-transform: uppercase; letter-spacing: 0.5px;
  }
  .spine-text .spine-author { font-size: 8px; color: var(--text-dark); margin-right: 8px; }
  .spine-band { position: absolute; left: 0; right: 0; bottom: 0; height: 26px; background: var(--band-blue); }
</style>
</head>
<body>
<main class="cover-spread">

  <section class="back-cover">
    <div class="sky-photo" role="img" aria-label="Blue sky with white clouds"></div>
    <div class="money-photo" role="img" aria-label="A sea of scattered banknotes stretching to the horizon"></div>
    <header class="title-block">
      <span class="author-possessive">MARTIN VARROW'S</span>
      <span class="title-line small title-outline">An Integrated Path</span>
      <span class="title-line large title-outline">To Operational</span>
      <span class="title-line small title-outline">Results Growth</span>
      <p class="subtitle">Shape a Steady Progress method<br>to match your workplace values</p>
    </header>
    <div class="also-known-panel">
      <p class="intro">Business Performance Improvement is also known as or can include:</p>
      <ul>
        <li>Continuous Improvement</li>
        <li>Process Improvement</li>
        <li>Lean Six Sigma</li>
        <li>Operational Excellence</li>
        <li>Total Productive Maintenance</li>
        <li>Harlow Assembly Method</li>
        <li>Total Quality Management</li>
        <li>Business Process Reengineering</li>
        <li>Output Levers</li>
        <li>=</li>
      </ul>
      <p class="company-result">Varrow Global</p>
    </div>
    <div class="publisher-mark">
      <span class="mark-dot"></span>
      <span class="mark-name">Varrow Global</span>
    </div>
    <div class="isbn-box">ISBN</div>
    <div class="back-band"></div>
  </section>

  <section class="spine">
    <div class="sky-photo" role="img" aria-label="Sky continuing across the spine"></div>
    <div class="money-photo" role="img" aria-label="Banknotes continuing across the spine"></div>
    <p class="spine-text"><span class="spine-author">Martin Varrow's</span>An Integrated Path to Operational Results Growth</p>
    <div class="spine-band"></div>
  </section>

  <section class="front-cover">
    <div class="sky-photo" role="img" aria-label="Blue sky with white clouds"></div>
    <div class="money-photo" role="img" aria-label="A sea of scattered banknotes stretching to the horizon"></div>
    <div class="boat-photo" role="img" aria-label="A businessman sailing ahead in a paper boat folded from a banknote, riding above the sea of money as a sign of progress and growth"></div>
    <header class="title-block">
      <span class="title-line small title-outline">An Integrated Path</span>
      <span class="title-line large title-outline">To Operational</span>
      <span class="title-line small title-outline">Results Growth</span>
      <p class="subtitle">Shape a Steady Progress method<br>to match your workplace values</p>
    </header>
    <footer class="author-band">MARTIN VARROW B. MECH ENG., M. SC (HVI)</footer>
  </section>

</main>
</body>
</html>
```